Restorative Fitness & Nutrition eBook

This is a simple nutrition ebook called Replenix. Designed to be download by athletes and fitness enthusiasts who want to improve their athletic performance and recovery after workouts.

This is one of 7 x e-book drafts ready to be designed up.

3 of them (including Replenix) are only 3-4 pages long, the other 4 ebooks are much longer and more comprehensive (15-40pages).

I am a restorative health and fitness coach based in Sydney. I work closely with athletes (runners and triathletes) to improve flexibility, core strength, breathing and mindset. I incorporate practices such as yoga, pilates, self-myofascial release, nutrition and meditation.

The ebooks will be available for purchase online and used for home study or training by my clients. They will have instructional photos and copy.

Target Market(s)

Everyday athletes. Runners. Triathletes. Swimmers. Fitness enthusiasts. Health conscious individuals. Aged between 30-50. A mix of male and female, but mostly women.

Industry/Entity Type

Fitness

Font styles to use
Sans Serif
Other font styles liked:
• Freeland Font

Requirements
Must have
• - Be visually beautiful using imagery supplied. I have more if needed.
• - The copy included
• - My logo
• - Short and sweet style. No more than 5 pages. Ideally 3-4
• - Light, white and fresh look
• - Clear and easy to read
Should not have
• Dark black themes
• Squishy text and no white space.

```html
<!DOCTYPE html>
<html lang="en">
<head>
<meta charset="utf-8">
<title>Replenix – Nourishing recipes</title>
<link href="https://fonts.googleapis.com/css2?family=Noto+Serif:ital,wght@0,400;0,700;1,400;1,700&family=Caveat:wght@600&family=Open+Sans:wght@400;600&display=swap" rel="stylesheet">
<style>
:root{
  --backdrop:#464c3c;
  --accent:#d9473c;
  --pink:#e08aa6;
  --ink:#2d2a28;
  --muted:#5d5a55;
  --panel:rgba(255,255,255,.74);
  --white:#ffffff;
}
*{margin:0;padding:0;box-sizing:border-box}
html,body{width:1200px;height:1146px;overflow:hidden;background:var(--backdrop)}
body{position:relative;font-family:"Noto Serif",Georgia,serif;color:var(--ink)}
.page{position:absolute;width:345px;height:488px;overflow:hidden;background:var(--white)}
.photo{position:absolute;left:0;width:100%}
.photo.top{top:0;height:244px}
.photo.bottom{top:244px;height:244px}
.photo.full{top:0;height:100%}

/* cover */
.cover .title{position:absolute;left:28px;top:70px;font-size:56px;color:var(--pink);font-weight:400;letter-spacing:1px}
.cover .tagline{position:absolute;left:28px;top:226px;font-size:13px;line-height:18px;font-style:italic;color:var(--muted)}
.cover .quote{position:absolute;left:22px;top:400px;width:118px;text-align:center;font-size:10px;line-height:14px;font-style:italic;font-weight:700;color:var(--ink)}
.cover .quote cite{display:block;font-size:8px;font-weight:400;color:var(--muted);font-style:italic}

/* menu panels */
.panel{position:absolute;left:27px;width:289px;background:var(--panel);border-radius:10px;padding:19px 8px 6px}
.pill{position:absolute;left:50%;top:5px;transform:translateX(-50%);background:var(--accent);color:var(--white);font-size:7px;font-weight:700;letter-spacing:.3px;padding:2px 14px;border-radius:8px;white-space:nowrap}
.meal{margin-bottom:6px}
.meal:last-child{margin-bottom:0}
.meal .when{display:block;font-size:5.6px;font-style:italic;font-weight:700;color:var(--accent)}
.meal .dish{display:block;font-size:5.8px;font-weight:700}
.meal p{font-size:5.5px;line-height:1.38}
.plate-title{position:absolute;left:78px;top:25px;width:190px;height:25px;background:rgba(255,255,255,.8);border-radius:6px;font-family:"Caveat",cursive;font-size:22px;line-height:25px;text-align:center;color:var(--accent)}

.lead{font-size:5.6px;font-style:italic;font-weight:700;color:var(--accent);margin-bottom:2px}
.list{list-style:none;font-size:5.5px;line-height:1.38;margin-bottom:6px}
.list li{padding-left:22px;position:relative}
.list li::before{content:"-";position:absolute;left:10px}
.pill.inline{position:relative;left:auto;top:auto;transform:none;display:table;margin:4px auto 6px}

.contact{position:absolute;left:0;top:414px;width:100%;text-align:center;font-family:"Open Sans",sans-serif;font-size:5.5px;line-height:8.3px;color:var(--white)}
.contact strong{font-weight:600}
</style>
</head>
<body>

<!-- Cover -->
<section class="page cover" style="left:60px;top:75px">
  <div class="photo full" role="img" aria-label="Smiling woman leaning on a white beach-house wall on a wooden boardwalk, holding a jar of yoghurt and berries" style="background:linear-gradient(90deg,#f1efe9 0%,#e9e5dc 45%,#cfc6b4 75%,#b9ad99 100%)"></div>
  <h1 class="title">Replenix</h1>
  <p class="tagline">Nourishing recipes to<br>feed your tired and<br>hungry muscles.</p>
  <blockquote class="quote">'Eat food,<br>not too much and<br>mostly plants'<cite>-Marcus Pell</cite></blockquote>
</section>

<!-- Monday / Tuesday -->
<section class="page" style="left:423px;top:75px">
  <div class="photo top" role="img" aria-label="Bowl of plums on a weathered wooden table" style="background:radial-gradient(circle at 50% 45%,#4e5378 0%,#6c6d86 35%,#9a9893 70%,#b7b3ab 100%)"></div>
  <div class="photo bottom" role="img" aria-label="Purple and green cabbage leaves" style="background:radial-gradient(circle at 50% 70%,#b69cc0 0%,#8a76a0 30%,#5d7f57 65%,#3f5f3f 100%)"></div>
  <div class="plate-title">7-days on my plate</div>
  <div class="panel" style="top:51px;height:182px">
    <span class="pill">MONDAY</span>
    <div class="meal"><span class="when">Breakfast</span><span class="dish">Power Protein Smoothie</span><p>I blend up 1 serving of protein powder, ½ tsp. of ground cinnamon, 1 tbsp. of chia seeds, ½ cup frozen berries, ½ frozen banana, ½ cup spinach leaves and 1 cup of nut or coconut milk.</p></div>
    <div class="meal"><span class="when">Lunch</span><span class="dish">Superfood Bowl</span><p>I chop and roast sweet potato and eggplant; steam shredded kale and chopped broccoli; and mix chopped coriander and mint through cooked quinoa. Add all cooked ingredients to a bowl, drizzle with tahini, top with chopped almonds and a tbsp. of sauerkraut. It's a big dose of vitamins, protein and gut lovin goodness.</p></div>
    <div class="meal"><span class="when">Dinner</span><span class="dish">Soba Noodle Special</span><p>I steam snow peas and frozen green edamame, spiralise a fresh carrot, and mix it all through cooked buckwheat soba noodles. I make a yummy Asian dressing by mixing ¼ cup tamari, 1 tbsp peanut butter, 1 tsp ginger, 1 tsp seasame oil, and the juice of a lime, and then I stir it through the noodles and veg and season with chopped coriander and toasted sesame seeds. Add some cooked tempeh or wild caught grilled salmon for extra protein.</p></div>
  </div>
  <div class="panel" style="top:275px;height:190px">
    <span class="pill">TUESDAY</span>
    <div class="meal"><span class="when">Breakfast</span><span class="dish">Overnight Oats</span><p>The night before I blend 1 banana with 1 tbsp. chia seeds, 1tsp. cinnamon, 1 serving of protein powder, ½ tbsp. of cacao powder and 1 cup of nut milk or water. Then I pour it in a jar and stir through ½ cup of oats. After letting it soak overnight, I enjoy it after my morning run.</p></div>
    <div class="meal"><span class="when">Lunch</span><span class="dish">Falafel Wrap</span><p>I spread beetroot and hummus dip on a Lebanese bread wrap, and then I fill it with lots of salad goodness (spinach, tomato, cucumber, sauerkraut, pickles, grated carrot) and 2-3 warm falafel balls. Wrap, eat and enjoy!</p></div>
    <div class="meal"><span class="when">Dinner</span><span class="dish">Mexican Bowl</span><p>I cook brown rice and my red kidney bean chili (1-can red kidney beans, ½ diced brown onion, 1 tsp. garlic, 1 grated zucchini, 1 grated carrot, 1 can of diced tomatoes, ½ tsp. chili powder). I fill a bowl with a serving of cooked brown rice, kidney bean chili, a handful of spinach leaves, chopped coriander and a huge dollop of my famous guacamole!</p></div>
  </div>
</section>

<!-- Wednesday / Thursday -->
<section class="page" style="left:60px;top:583px">
  <div class="photo top" role="img" aria-label="Colander of green beans on a rustic teal metal tray" style="background:radial-gradient(circle at 45% 50%,#7f9a6a 0%,#5f7a6d 40%,#4d6663 75%,#6d6a5f 100%)"></div>
  <div class="photo bottom" role="img" aria-label="Vegetables cooking in a wok over a gas flame" style="background:radial-gradient(circle at 35% 70%,#a76b3f 0%,#6b4a36 35%,#3d3330 70%,#2c2624 100%)"></div>
  <div class="panel" style="top:39px;height:171px">
    <span class="pill">WEDNESDAY</span>
    <div class="meal"><span class="when">Breakfast</span><span class="dish">Toast and Banana</span><p>I toast some soughdough bread and top it with with peanut or almond butter and sliced banana. Easy peasy!</p></div>
    <div class="meal"><span class="when">Lunch</span><span class="dish">Salad and Mixed Bean Wrap</span><p>I spread beetroot and hummus dip on a Lebanese bread wrap, and then I fill it with lots of salad goodness (spinach, tomato, cucumber, sauerkraut, pickles, grated carrot) and any leftover beans I may have (the four-bean mix is great!).</p></div>
    <div class="meal"><span class="when">Dinner</span><span class="dish">Roast Veggie Red Curry with Quinoa</span><p>I chop and roast sweet potato and sliced red capsicum, then I steam green peas and broccoli florets. I gently fry 2 tbsp. of red curry paste with 1 can of coconut milk then I add all the cooked veggies and let it simmer for 10-mins. Spoon it over cooked quinoa and garnish with</p></div>
  </div>
  <div class="panel" style="top:276px;height:179px">
    <span class="pill">THURSDAY</span>
    <div class="meal"><span class="when">Breakfast</span><span class="dish">Power Protein Smoothie</span><p>I blend up 1 serving of protein powder, ½ tsp. of ground cinnamon, 1 tbsp. of chia seeds, ½ cup frozen berries, ½ frozen banana, ½ cup spinach leaves and 1 cup of nut or coconut milk.</p></div>
    <div class="meal"><span class="when">Lunch</span><span class="dish">Stuffed Sweet Potato</span><p>I wash a small sweet potato (keep the skin on). With a fork, poke holes all over potato and wrap in a paper towel. I microwave the sweet potato on high for about 8 minutes, or until tender all the way to the center. Cut the potato in half and top it with a handful of rocket and leftover lentils. Microwave uncovered for 30 seconds to wilt rocket and warm lentils. Top with cinnamon, dried thyme, dried cranberries, pumpkin seeds and a drizzle of olive oil.</p></div>
    <div class="meal"><span class="when">Dinner</span><span class="dish">Spaghetti with Green Pesto and Roast Cherry Tomatoes</span><p>I cook a serving of whole-wheat spaghetti and roast a handful of cherry tomatoes in the oven. In a bowl I add the cooked pasta, the roast cherry tomatoes and stir through 2-heaped tbsp. of my homemade pesto. Add a squeeze of lemon and salt and pepper to finish.</p></div>
  </div>
</section>

<!-- Friday / Saturday -->
<section class="page" style="left:423px;top:583px">
  <div class="photo top" role="img" aria-label="Jar of granola with nuts and dried fruit on a wooden board" style="background:radial-gradient(circle at 50% 55%,#8c6a4f 0%,#a89580 35%,#b9b0a3 65%,#8a8c8e 100%)"></div>
  <div class="photo bottom" role="img" aria-label="Two halves of a blood orange" style="background:radial-gradient(circle at 50% 50%,#f3c59a 0%,#ee8a52 30%,#e2542f 65%,#b33a22 100%)"></div>
  <div class="panel" style="top:39px;height:180px">
    <span class="pill">FRIDAY</span>
    <div class="meal"><span class="when">Breakfast</span><span class="dish">Gluten Free Granola</span><p>I start the day with ½ cup of my homemade gluten free granola, topped with fresh berries, seeds, coconut yoghurt and almond milk.</p></div>
    <div class="meal"><span class="when">Lunch</span><span class="dish">Spinach, Roast Pumpkin and Chickpea Salad</span><p>I roast chopped pumpkin that has been seasoned with salt, pepper and cumin. Then I mix baby spinach, canned chickpeas, finely sliced red onion, chopped figs and the roast pumpkin in a bowl. After mixing all together, I season with chopped coriander, olive oil and salt and pepper.</p></div>
    <div class="meal"><span class="when">Dinner</span><span class="dish">Veggie Pad Thai</span><p>Stir-fry matchstick cut carrot sticks, red capsicum sticks and broccoli florets in coconut oil. Cook rice noodles as per directions and mix ingredients together with my favourite Asian dressing, ¼ cup tamari, 1 tbsp. peanut butter, 1 tsp. ginger, 1 tsp. sesame oil, and the juice of a lime. Then I season with chopped coriander and chopped spring onions. Add some cooked tempeh or lean grilled chicken for extra protein.</p></div>
  </div>
  <div class="panel" style="top:288px;height:155px">
    <span class="pill">SATURDAY</span>
    <div class="meal"><span class="when">Breakfast</span><span class="dish">Green Machine</span><p>I scramble 2 free range eggs with 1-heaped tbsp. of my homemade pesto. Serve with soughdough toast and avocado, et voila!</p></div>
    <div class="meal"><span class="when">Lunch</span><span class="dish">Sushi</span><p>Lunch is on the go today and I choose take-away brown rice and vegetable sushi.</p></div>
    <div class="meal"><span class="when">Dinner</span><span class="dish">Homemade Burger and Chips</span><p>I make sweet potato and lentil patties and build a burger on a wholegrain roll with salad greens, sliced tomato, beetroot, pickles and cucumber. You can also roast some homemade potato fries on the side if you're starving. Every now and then I'll use lean beef mince instead of the beans if I need more iron.</p></div>
  </div>
</section>

<!-- Sunday / Snacks / Drinks -->
<section class="page" style="left:787px;top:583px">
  <div class="photo full" role="img" aria-label="Open book on a table beside a wrist with a watch and a bowl of grains" style="background:linear-gradient(180deg,#9aa0a6 0%,#7c8189 30%,#5b5a57 60%,#3b3733 100%)"></div>
  <div class="panel" style="top:39px;height:167px">
    <span class="pill">SUNDAY</span>
    <div class="meal"><span class="when">Breakfast</span><span class="dish">Buckwheat Banana Pancakes</span><p>Blend well all ingredients: 1 cup nut or coconut milk, 1 ripe banana, 1/2 tsp. vanilla, 1 tbsp. coconut oil, 1 cup buckwheat flour, 1 tsp. baking powder and a pinch of sea salt. Cook both sides using some baking paper on skillet or pan then top it with maple syrup, coconut yoghurt, seeds and sprinkle with cinnamon.</p></div>
    <div class="meal"><span class="when">Lunch</span><span class="dish">Left Overs</span><p>I eat the left over burger patties from last night with a green salad on the side.</p></div>
    <div class="meal"><span class="when">Dinner</span><span class="dish">Roast Veggie Lasagna</span><p>This is one for the family. I roast a stack of vegetables (sweet potato, pumpkin, zucchini, capsicum, eggplant). Then I layer a baking dish with the roast veggies, tomato passata sauce, spinach leaves and whole-wheat lasagna sheets. To finish I top with a ricotta and Parmesan cheese.</p></div>
  </div>
  <div class="panel" style="top:230px;height:174px;padding-top:19px">
    <span class="pill">SNACKS</span>
    <p class="lead">If I'm on the run or feeling extra hungry I reach for:</p>
    <ul class="list">
      <li>Fresh carrot sticks with hummus</li>
      <li>Brown rice crackers with either almond/peanut butter, avocado or hummus spread on top</li>
      <li>A piece of whole fruit…whatever is in season</li>
      <li>A handful of mixed nuts and seeds</li>
      <li>2 x fresh dates. I like to take the pit out and stuff a macadamia in the middle.</li>
      <li>A few tablespoons of coconut yoghurt with fresh berries and a sprinkle of cinnamon.</li>
    </ul>
    <span class="pill inline">DRINKS</span>
    <ul class="list">
      <li>I drink water, and lots of it.</li>
      <li>Earl grey tea in the morning and decaf green tea in the afternoon.</li>
      <li>On the weekends I usually have a green juice with lots of fruit and veggies for a potent vitamin hit.</li>
      <li>I love a glass of wine with dinner on the weekends.</li>
    </ul>
  </div>
  <footer class="contact">
    <strong>Learn more</strong><br>www.lenahart.com<br>
    <strong>Let's connect</strong><br>lena@lenahart.com | Facebook @LenaHart | Instagram @lenahartfit<br>
    <strong>Let's work together</strong><br>1:1 Coaching | Online Coaching | Workshops | E-Resources
  </footer>
</section>

</body>
</html>
```